Premium Lawn fertiliser packaging - Looking for long term designer

*Update at bottom
I need a carefully considered, bold and professional packaging design for my new premium lawn fertiliser product. This contest is for a detailed front of the stand-up pouch packaging and once I’ve chosen a winner, they’ll be asked to create the layout for the back that links to the front as well. I have a full range of additional products that will also need designs and so I'm looking for someone who can do a great job here and who we can work with long term.

The front should include our logo for Brindley Turf Supply Direct and be titled “Meadow Rise Max” "Professional Lawn Fertiliser". The spring fertiliser tag line is "Awaken your lawn: Lush Greening, Lasting Health".
Beneath it, it then needs to include some important usage information and the key benefits along with some suitable graphic.

Key information to include:

Apply March - June
Treats 35-50 m2
16-3-8
+2%MgO + 1% Fe + 2.9% CaO (this is the chemical makeup of the fertiliser and needs to be fairly prominent. If you look at other professional fertiliser packaging, you'll see how it needs to compare).

Key features:
Premium fertiliser, used by professionals
Advanced greening with micro-nutrient complex
Dual action Nitrogen: Instant green boost & continuous feed for 3 months
Child & pet safe

Our brand colours are purple and green. Purple = #592999, Green = 3cb64a / 81d742 / 4d9d44

I think these colours look great against a white background.

Please make sure you look at our website as well to get an idea of our brand: www.brindleyturfsupply.co.uk

To help, I've attached images of competitors fertiliser packaging that I like the look of. I'm not looking for you to copy but just see what type of thing appeals to me, the standard I'm expecting and what I need to compete against....

In addition, I have also attached some potential images you may wish to try using in your design, although please feel free to use your own if you have something better. For the moment, the images are 'preview' images, but once I decide on a design and we agree on the correct image, I will download and send over a fully licensed version.

*** Update*** When submitting your design, can you submit it in 2 formats: The first as a fully printed custom stand-up pouch and the second as a full-size label stuck onto a standup pouch (whatever colour you think is right for your design - choose white if you are not sure). To explain, I've just discovered we won't be able to get full custom bags printed in time for the first run and so we will have to opt for the design to be printed on labels and fixed onto bags. I therefore need to choose a design that works in both formats as both a label on a standup pouch as well as a fully printed pouch. Many thanks.

Target Market(s)

Domestic home-owners

Industry/Entity Type

Lawn care. NOT AGRICULTURE OR FARMING

Font styles to use
Sans Serif

Requirements
Must have
• Presented in 2 formats - see update at bottom of description
Nice to have
• I quite like designs against a white background, although I’m open to other ideas as well.
Should not have
• Please do not include any people or faces in the design. The text should be solid in colour, so no graduated colour fill in the text or outline text. Please avoid over-busy or cluttered designs.

```html
<!DOCTYPE html>
<html lang="en">
<head>
<meta charset="utf-8">
<title>Meadow Rise Max – Professional Lawn Fertiliser Label</title>
<link href="https://fonts.googleapis.com/css2?family=Anton&family=Michroma&family=Montserrat:wght@300;400;500;600;700;800&display=swap" rel="stylesheet">
<style>
  :root{
    --bg:#eceeea;
    --paper:#ffffff;
    --green:#4d9d44;
    --green-bright:#5cb82e;
    --green-light:#81d742;
    --brown:#3b2a1f;
    --soil:#3a2717;
    --soil-dark:#2b1c10;
    --ink:#2d2a26;
    --white:#ffffff;
  }
  *{margin:0;padding:0;box-sizing:border-box}
  html,body{width:1200px;height:2400px;overflow:hidden}
  body{background:var(--bg);font-family:"Montserrat",sans-serif;position:relative}

  .label{position:absolute;left:30px;top:235px;width:1140px;height:1930px;background:var(--paper);overflow:hidden;box-shadow:0 10px 40px rgba(0,0,0,.12)}
  .center{position:absolute;left:0;width:100%;text-align:center}

  .brand{top:230px;display:flex;justify-content:center;align-items:center;gap:22px}
  .brand-dot{width:60px;height:60px;border-radius:50%;background:var(--green-bright)}
  .brand-name{font-family:"Montserrat",sans-serif;font-weight:700;color:var(--brown);font-size:48px;line-height:1.05;text-align:left;letter-spacing:1px}
  .brand-name span{display:block;font-size:27px;letter-spacing:5px}

  .product-title{top:490px;font-family:"Anton",sans-serif;font-size:140px;line-height:1;color:var(--green-bright);letter-spacing:1px}
  .product-sub{top:648px;font-family:"Michroma",sans-serif;font-size:60px;line-height:1;color:var(--brown);font-weight:700;-webkit-text-stroke:1.5px var(--brown)}
  .product-type{position:absolute;left:148px;top:720px;width:866px;height:84px;background:var(--brown);color:var(--white);font-family:"Michroma",sans-serif;font-size:60px;display:flex;align-items:center;justify-content:center;letter-spacing:4px;-webkit-text-stroke:1px var(--white)}
  .tagline{top:822px;font-family:"Montserrat",sans-serif;font-weight:400;font-size:42px;letter-spacing:9px;color:var(--ink);line-height:1}
  .tagline-green{top:868px;font-weight:500;font-size:36px;letter-spacing:7px;color:var(--green-bright)}

  .features{position:absolute;left:132px;top:968px;width:220px;list-style:none;text-align:center}
  .feature{height:178px;display:flex;flex-direction:column;align-items:center;font-size:19px;line-height:1.2;color:var(--ink)}
  .feature strong{font-weight:700}
  .feature svg{width:72px;height:72px;margin-bottom:10px}

  .scene{position:absolute;left:360px;top:915px;width:750px;height:690px;border-radius:45% 45% 48% 48% / 35% 35% 30% 30%;background:radial-gradient(ellipse at 50% 35%,#9a8f7e 0%,#6d6a5c 35%,#4f8a35 62%,#2f6a22 100%)}

  .safe-badge{position:absolute;left:395px;top:996px;width:180px;height:204px}

  .soil{position:absolute;left:0;top:1520px;width:1140px;height:410px}

  .apply{top:1630px;font-family:"Michroma",sans-serif;font-size:44px;color:var(--white);letter-spacing:1px;-webkit-text-stroke:1px var(--white)}
  .analysis{position:absolute;left:180px;top:1690px;width:750px;height:58px;background:var(--white);display:flex;align-items:center;justify-content:center;font-family:"Montserrat",sans-serif;font-weight:800;font-size:44px;color:var(--brown);letter-spacing:2px}
  .specs{top:1762px;display:flex;justify-content:center;gap:46px;color:var(--white);font-size:36px;font-weight:400}
  .specs .tick{color:var(--green-bright);font-weight:800;margin-right:6px}
  .weight{top:1822px;font-size:30px;color:var(--green-bright);font-weight:400;letter-spacing:1px}
  .weight b{color:var(--white);font-weight:800;font-size:46px}
  .weight small{color:var(--white);font-weight:800;font-size:30px}
</style>
</head>
<body>
<main class="label">

  <div class="center brand">
    <div class="brand-dot"></div>
    <div class="brand-name">Brindley<span>TURF SUPPLY DIRECT</span></div>
  </div>

  <h1 class="center product-title">MEADOW RISE MAX</h1>
  <div class="center product-sub">PROFESSIONAL</div>
  <div class="product-type">LAWN FERTILISER</div>
  <p class="center tagline">AWAKEN YOUR LAWN</p>
  <p class="center tagline tagline-green">LUSH GREENING, LASTING HEALTH</p>

  <ul class="features">
    <li class="feature">
      <svg viewBox="0 0 72 72"><circle cx="36" cy="36" r="34" fill="#3f8f2e"/><circle cx="36" cy="36" r="28" fill="none" stroke="#fff" stroke-width="2"/><path d="M24 32 L30 24 H42 L48 32 L36 48 Z M24 32 H48 M30 24 L36 48 L42 24" fill="none" stroke="#fff" stroke-width="2" stroke-linejoin="round"/></svg>
      <span><strong>Premium fertiliser</strong><br>used by<br>professionals</span>
    </li>
    <li class="feature">
      <svg viewBox="0 0 72 72"><circle cx="36" cy="36" r="34" fill="#3f8f2e"/><circle cx="36" cy="36" r="28" fill="none" stroke="#fff" stroke-width="2"/><path d="M24 46 L28 30 L32 46 M32 46 L36 24 L40 46 M40 46 L44 30 L48 46 M22 46 H50" fill="none" stroke="#fff" stroke-width="2" stroke-linejoin="round"/></svg>
      <span><strong>Advanced greening</strong><br>with micro-nutrient<br>complex</span>
    </li>
    <li class="feature">
      <svg viewBox="0 0 72 72"><circle cx="36" cy="36" r="34" fill="#3f8f2e"/><circle cx="36" cy="36" r="28" fill="none" stroke="#fff" stroke-width="2"/><path d="M22 44 Q30 40 36 44 H46 M22 50 H44 L52 42 M38 38 V28 M38 30 Q32 24 30 28 Q34 32 38 30 M38 30 Q44 22 46 26 Q42 32 38 30" fill="none" stroke="#fff" stroke-width="2" stroke-linejoin="round"/></svg>
      <span><strong>Dual action Nitrogen:</strong><br>Instant green boost &amp;<br>continuous feed<br>for 3 months</span>
    </li>
  </ul>

  <div class="scene" role="img" aria-label="Stone country house with a striped green lawn and flower beds on a round turf base"></div>

  <svg class="safe-badge" viewBox="0 0 180 204" aria-label="Child and pet safe">
    <path d="M90 4 Q130 20 174 18 V100 Q170 160 90 200 Q10 160 6 100 V18 Q50 20 90 4 Z" fill="#ffffff" stroke="#3b2a1f" stroke-width="5"/>
    <path d="M90 16 Q126 30 162 28 V100 Q158 150 90 186 Q22 150 18 100 V28 Q54 30 90 16 Z" fill="#5cb82e"/>
    <text x="90" y="138" text-anchor="middle" font-family="Montserrat, sans-serif" font-weight="800" font-size="17" fill="#fff">CHILD &amp; PET</text>
    <text x="90" y="158" text-anchor="middle" font-family="Montserrat, sans-serif" font-weight="800" font-size="17" fill="#fff">SAFE</text>
  </svg>

  <svg class="soil" viewBox="0 0 1140 410" preserveAspectRatio="none">
    <path d="M0 150 Q540 -40 1140 40 V410 H0 Z" fill="#5cb82e"/>
    <path d="M0 180 Q540 10 1140 70 V410 H0 Z" fill="#3a2717"/>
  </svg>

  <div class="center apply">APPLY MARCH - JUNE</div>
  <div class="analysis">+2%MGO + 1% FE + 2.9% CAO</div>
  <div class="center specs"><span><span class="tick">✓</span>Treats 35-50 m2</span><span><span class="tick">✓</span>16-3-8</span></div>
  <div class="center weight">NETWT. <b>10</b><small>LBS</small> &nbsp;COVERS UP TO <b>2500</b><small>SQFT.</small></div>

</main>
</body>
</html>
```